Business Card Design for Technology Company

New business card design needed for technology company director.
Ideally, the design will fit the style and nature of the industry. We are a supplier of quality products and services, and we hope the design will give customers and suppliers this impression.

Target Market(s)

3D Printing Industry

Industry/Entity Type

Technology Equipment

Contact Information for Business Card

Name: Marcus Lyle
Title: Director
Company address: Factory K4, 7B Morland Road, Brookmere Eastland Australia 7311
Telephone: +61-7-4290 6413
Email: marcus.lyle@veranox.com.au
Website: www.veranox.com.au

Requirements
Must have
• All information in business card details
• Company logo
• '3D Printers and 3D Print Filaments' at proper place
Nice to have
• Style to fit the industry
• Colour to fit logo

```html
<!DOCTYPE html>
<html lang="en">
<head>
<meta charset="utf-8">
<title>Veranox Technology – Business Card</title>
<link rel="stylesheet" href="https://fonts.googleapis.com/css2?family=Open+Sans:wght@300;400;600;700&display=swap">
<style>
  :root {
    --backdrop: #3b3330;
    --card: #1c1e21;
    --card-edge: #26292d;
    --ink: #f2f2f2;
    --blue: #1f74c8;
    --orange: #f28c1e;
    --rule: #8a8f96;
  }
  * { box-sizing: border-box; margin: 0; padding: 0; }
  html, body { width: 1200px; height: 864px; overflow: hidden; }
  body {
    background: var(--backdrop);
    font-family: "Open Sans", Arial, sans-serif;
    display: flex;
    align-items: center;
    justify-content: center;
    gap: 40px;
  }
  .card {
    width: 550px;
    height: 336px;
    background: linear-gradient(160deg, var(--card-edge), var(--card));
    border-radius: 4px;
    box-shadow: 0 12px 30px rgba(0,0,0,.45);
    position: relative;
    color: var(--ink);
  }

  /* Front */
  .card--front .brand {
    position: absolute;
    left: 150px; top: 96px;
    display: flex; align-items: center; gap: 16px;
  }
  .brand-mark {
    width: 46px; height: 46px;
    background: var(--orange);
    border-radius: 4px;
  }
  .brand-name {
    font-weight: 600;
    font-size: 30px;
    letter-spacing: 6px;
    line-height: 1.1;
    color: var(--ink);
  }
  .brand-name small {
    display: block;
    font-size: 10px;
    letter-spacing: 7px;
  }
  .tagline {
    position: absolute;
    left: 0; right: 0; bottom: 92px;
    text-align: center;
    font-weight: 300;
    font-size: 15px;
    letter-spacing: 4px;
    color: var(--ink);
  }

  /* Back */
  .card--back .brand {
    position: absolute;
    left: 34px; top: 118px;
    width: 190px;
    display: flex; flex-direction: column; align-items: center; gap: 16px;
  }
  .card--back .brand-name { font-size: 26px; letter-spacing: 5px; text-align: center; }
  .card--back .brand-name small { font-size: 9px; letter-spacing: 6px; }
  .divider {
    position: absolute;
    left: 244px; top: 50px; bottom: 50px;
    width: 1px;
    background: linear-gradient(to bottom, transparent, var(--rule), transparent);
  }
  .contact {
    position: absolute;
    left: 268px; top: 74px; right: 20px;
    font-size: 13px;
    line-height: 1.45;
  }
  .contact-name {
    color: var(--blue);
    font-weight: 700;
    font-size: 19px;
    text-transform: uppercase;
    line-height: 1.1;
  }
  .contact-role {
    color: var(--orange);
    font-size: 14px;
    text-transform: uppercase;
    margin-bottom: 8px;
  }
  .contact-line { display: flex; align-items: center; gap: 7px; }
  .contact-line svg { width: 12px; height: 12px; fill: var(--blue); flex: none; }
  .address { margin-bottom: 2px; }
</style>
</head>
<body>
  <section class="card card--front">
    <div class="brand">
      <span class="brand-mark"></span>
      <span class="brand-name">VERANOX<small>TECHNOLOGY</small></span>
    </div>
    <p class="tagline">3D Printers and 3D Print Filaments</p>
  </section>

  <section class="card card--back">
    <div class="brand">
      <span class="brand-mark"></span>
      <span class="brand-name">VERANOX<small>TECHNOLOGY</small></span>
    </div>
    <div class="divider"></div>
    <div class="contact">
      <p class="contact-name">Marcus Lyle</p>
      <p class="contact-role">Director</p>
      <p class="address">Factory K4, 7B Morland Road,<br>Brookmere Eastland<br>Australia 7311</p>
      <p class="contact-line">
        <svg viewBox="0 0 24 24" aria-hidden="true"><path d="M6.6 10.8a15 15 0 0 0 6.6 6.6l2.2-2.2a1 1 0 0 1 1-.25 11.4 11.4 0 0 0 3.6.57 1 1 0 0 1 1 1V20a1 1 0 0 1-1 1A17 17 0 0 1 3 4a1 1 0 0 1 1-1h3.5a1 1 0 0 1 1 1c0 1.25.2 2.45.57 3.6a1 1 0 0 1-.25 1z"/></svg>
        +61-7-4290 6413
      </p>
      <p class="contact-line">
        <svg viewBox="0 0 24 24" aria-hidden="true"><path d="M2 5h20v14H2z M2 5l10 8 10-8" /></svg>
        marcus.lyle@veranox.com.au
      </p>
      <p class="contact-line">
        <svg viewBox="0 0 24 24" aria-hidden="true"><path d="M12 2a7 7 0 0 0-7 7c0 5 7 13 7 13s7-8 7-13a7 7 0 0 0-7-7zm0 9.5A2.5 2.5 0 1 1 12 6.5a2.5 2.5 0 0 1 0 5z"/></svg>
        www.veranox.com.au
      </p>
    </div>
  </section>
</body>
</html>
```